Management Consulting needing a cool business card for client acquisition and networking

We are looking for a business card that is progressive and fresh that conveys innovation, forward thinking, and confidence. The business card is for a company based in Charlotte NC called, 'VELMORE CONSULTING GROUP LLC'. The company primarily works with banks, insurance, and brokerages to implement innovative solutions to help them streamline their operations, to more effectively manage risks, and to improve their customer relationships.

Target Market(s)

Typically meet with Chief Financial Officers, Chief Information Officers, Chief Operations Officer, Business Unit Leader. The target market are generally 40-55 years, male, white, master level education plus.

Industry/Entity Type

Progressive

Font styles to use
Serif
Other font styles liked:
• Calibri

Requirements
Should not have
• Designs that look too much like law firms or accounting companies. Too conservative

```html
<!DOCTYPE html>
<html lang="en">
<head>
<meta charset="utf-8">
<title>Velmore Consulting Group LLC — Business Card</title>
<link href="https://fonts.googleapis.com/css2?family=Carlito:wght@400;700&display=swap" rel="stylesheet">
<style>
  :root {
    --stage: #2b2b2b;
    --card-deep: #0b0b0b;
    --card-mid: #2a2a2a;
    --card-glow: #5a5a5a;
    --ink-bright: #ffffff;
    --ink-soft: #c9c9c9;
    --ink-muted: #a9a9a9;
    --ring: rgba(255, 255, 255, 0.85);
  }
  * { box-sizing: border-box; margin: 0; padding: 0; }
  html, body {
    width: 1200px;
    height: 1000px;
    overflow: hidden;
    background: var(--stage);
    font-family: "Carlito", "Calibri", sans-serif;
  }
  .canvas {
    position: relative;
    width: 1200px;
    height: 1000px;
  }
  .card {
    position: absolute;
    left: 239px;
    width: 687px;
    overflow: hidden;
    box-shadow: 0 6px 18px rgba(0, 0, 0, 0.45);
  }
  .card-texture {
    position: absolute;
    inset: 0;
  }
  .card--front { top: 67px; height: 419px; }
  .card--front .card-texture {
    background:
      radial-gradient(ellipse 55% 60% at 50% 38%, var(--card-glow) 0%, var(--card-mid) 45%, var(--card-deep) 100%);
  }
  .card--back { top: 550px; height: 381px; }
  .card--back .card-texture {
    background:
      radial-gradient(ellipse 70% 80% at 60% 45%, #4a4a4a 0%, var(--card-mid) 50%, var(--card-deep) 100%);
  }

  /* Front */
  .brand {
    position: absolute;
    left: 0;
    right: 0;
    top: 108px;
    display: flex;
    flex-direction: column;
    align-items: center;
  }
  .brand-mark {
    width: 86px;
    height: 86px;
    border: 2px solid var(--ring);
    border-radius: 50%;
  }
  .brand-name {
    margin-top: 46px;
    font-size: 25px;
    font-weight: 400;
    letter-spacing: 0.3px;
    color: var(--ink-soft);
  }

  /* Back */
  .backdrop-ring {
    position: absolute;
    left: 62px;
    top: 12px;
    width: 310px;
    height: 310px;
    border: 3px solid rgba(255, 255, 255, 0.12);
    border-radius: 50%;
  }
  .holder {
    position: absolute;
    right: 71px;
    top: 38px;
    text-align: right;
  }
  .holder-name {
    font-size: 41px;
    font-weight: 700;
    line-height: 1;
    color: var(--ink-bright);
  }
  .holder-title {
    margin-top: 6px;
    font-size: 25px;
    font-weight: 700;
    line-height: 1;
    color: var(--ink-muted);
  }
  .contact {
    position: absolute;
    right: 59px;
    top: 239px;
    list-style: none;
    text-align: right;
    font-size: 23px;
    line-height: 32px;
    color: var(--ink-muted);
  }
</style>
</head>
<body>
<main class="canvas">
  <section class="card card--front">
    <div class="card-texture" role="img" aria-label="Dark brushed wood plank texture with a soft central light"></div>
    <div class="brand">
      <div class="brand-mark"></div>
      <p class="brand-name">Velmore Consulting Group LLC</p>
    </div>
  </section>

  <section class="card card--back">
    <div class="card-texture" role="img" aria-label="Dark brushed wood plank texture"></div>
    <div class="backdrop-ring"></div>
    <div class="holder">
      <h1 class="holder-name">Daniel R. Moss</h1>
      <p class="holder-title">President</p>
    </div>
    <ul class="contact">
      <li>Tel o: 704.555.0182</li>
      <li>c: 704.555.0147</li>
      <li>dmoss@velmoreconsulting.com</li>
      <li>www.velmoreconsulting.com</li>
    </ul>
  </section>
</main>
</body>
</html>
```